VARNO - new private security company in Guyana, South America needs a website & logo design

New private security company in Guyana needs a website ready for the company launch. The business will offer armed and unarmed security to high net worth individuals, politicians, government officials, diplomats and off-shore oil industry vessels and platforms.

The company has its own heliport and indoor training range, armoured vehicles, ambulances and uniformed security personnel, and we would like some imager to indicate this.

The team leaders are all ex-special forces.

The website structure should be something like:

PAGE 1 Home
PAGE 2 About Us
PAGE 3 Guyana Security Overview
PAGE 4 Services
PAGE 5 Contact Us
PAGE 6 Useful Links

We have uploaded a file with the text copy for each of these pages.

The web domain has been registered through 456-dom and is www.varno.group

Target Market(s)

Corporations involved in the oil and gas industry, Embassies, Investment companies and individuals, Caribbean diaspora.

Industry/Entity Type

Security Service

Logo Text

VARNO

Coding

Coded - Design and coding required

Number of Pages Required

5+ page

Font styles to use
Sans Serif

Requirements
Must have
• Must have:
an enquiry/contact form page
general location map: https://mapz.example/loc/kP8wq2Lbnxv7hRt4;
text as per web content document uploaded to this site
Nice to have
• Images of private security (cars, bodyguards, helicopters/planes, etc)
Images of Maritime security (non-military)
Images of people of colour (Guyana has mainly afro and indian residents)
Image of a high tec security control room

```html
<!DOCTYPE html>
<html lang="en">
<head>
<meta charset="utf-8">
<title>VARNO – Private Security Guyana</title>
<link href="https://fonts.googleapis.com/css2?family=Montserrat:wght@500;600;700;800;900&family=Open+Sans:wght@400;600&family=Roboto:wght@400;500;700&display=swap" rel="stylesheet">
<style>
:root{
  --red:#e41d2d;
  --red-deep:#b51521;
  --ink:#1f2024;
  --ink-2:#26272c;
  --footer:#141416;
  --white:#ffffff;
  --muted:#c9c9cc;
}
*{margin:0;padding:0;box-sizing:border-box}
html,body{width:685px;height:1200px;overflow:hidden;background:var(--ink)}
body{position:relative;font-family:'Open Sans',sans-serif;color:var(--white)}
.abs{position:absolute}

/* hero */
.hero{position:absolute;left:0;top:0;width:685px;height:352px;background:var(--ink);overflow:hidden}
.hero-photo{position:absolute;left:230px;top:0;width:455px;height:352px;
  background:linear-gradient(90deg,var(--ink) 0%,rgba(31,32,36,.6) 20%,rgba(90,78,70,.5) 55%,rgba(175,160,150,.55) 100%),
  linear-gradient(180deg,#8a7a70 0%,#3a3a40 55%,#24252a 100%)}
.brand{left:99px;top:14px;display:flex;align-items:center;gap:5px;font-family:'Montserrat',sans-serif;font-weight:700;font-size:15px;letter-spacing:.5px}
.brand-dot{width:13px;height:13px;border-radius:50%;background:var(--red)}
.nav{left:216px;top:21px;display:flex;gap:11px;font-family:'Montserrat',sans-serif;font-weight:700;font-size:5.4px;letter-spacing:.1px}
.nav .active{position:relative}
.nav .active::after{content:"";position:absolute;left:0;right:0;top:11px;height:1px;background:var(--white)}
.phone{left:500px;top:19px;font-family:'Montserrat',sans-serif;font-size:7.8px;font-weight:500;letter-spacing:.3px}
.btn{display:flex;align-items:center;justify-content:center;border-radius:20px;background:var(--red);
  font-family:'Montserrat',sans-serif;font-weight:600;letter-spacing:.7px;color:var(--white);box-shadow:0 0 0 1.5px var(--ink),0 0 0 2.4px var(--red)}
.btn-call{left:492px;top:38px;width:93px;height:18px;font-size:6.4px}
.eyebrow{left:120px;top:131px;font-family:'Montserrat',sans-serif;font-weight:700;font-size:7.2px;letter-spacing:2.2px}
.hero-title{left:115px;top:136px;font-family:'Montserrat',sans-serif;font-weight:900;font-size:49px;letter-spacing:-.5px;line-height:1}
.hero-copy{left:120px;top:190px;width:160px;font-size:5.8px;line-height:7.3px}
.btn-more{left:122px;top:236px;width:93px;height:19px;font-size:6px}
.slides{left:303px;top:297px;display:flex;align-items:center;font-family:'Montserrat',sans-serif;font-size:6px;font-weight:600}
.slides .bar{width:20px;height:1px;background:var(--red);margin:0 3px}
.slides span.n{margin-right:12px}

/* badges */
.badge{width:38px;height:38px;border-radius:50%;background:var(--white);box-shadow:0 0 0 2px #ddd;display:flex;align-items:center;justify-content:center;z-index:3}
.badge i{width:18px;height:18px;border-radius:50%;background:var(--red)}

/* services */
.services{position:absolute;left:0;top:352px;width:685px;height:275px;overflow:hidden;
  background:linear-gradient(180deg,rgba(40,42,48,.55),rgba(30,32,38,.75)),linear-gradient(100deg,#6b6f73 0%,#3e4046 35%,#2e3036 60%,#4c4f56 100%)}
.section-title{font-family:'Montserrat',sans-serif;font-weight:900;font-size:21px;text-align:center;width:685px;left:0}
.services .section-title{top:54px}
.services .lead{left:0;width:685px;top:78px;text-align:center;font-size:7.6px;line-height:9.8px}
.svc{width:120px;text-align:center;top:123px}
.svc .ring{width:63px;height:63px;margin:0 auto;border-radius:50%;border:1.2px solid var(--white);display:flex;align-items:center;justify-content:center}
.svc .ring.on{background:var(--red);border-color:var(--red)}
.svc p{margin-top:14px;font-family:'Montserrat',sans-serif;font-weight:600;font-size:7px;letter-spacing:.9px;line-height:8.4px}
.arrow{top:143px}

/* about */
.about{position:absolute;left:0;top:627px;width:685px;height:259px;background:var(--ink);overflow:hidden}
.about-title{left:99px;top:32px;font-family:'Montserrat',sans-serif;font-weight:900;font-size:20.5px}
.about-title em{font-style:normal;color:var(--red)}
.about-rule{left:99px;top:64px;width:36px;height:1.5px;background:var(--white)}
.col{top:82px;width:172px;font-family:'Roboto',sans-serif;font-size:6.6px;line-height:9.7px;color:#eee}
.col p{margin-bottom:9.7px}
.about-photo{left:468px;top:3px;width:210px;height:256px;
  background:radial-gradient(ellipse at 55% 40%,#3a3d44 0%,#2c2e34 55%,rgba(31,32,36,0) 80%)}

/* contact */
.contact{position:absolute;left:0;top:886px;width:685px;height:177px;overflow:hidden;
  background:linear-gradient(90deg,var(--red) 0%,var(--red) 45%,#c4182a 65%,#a7131f 80%,var(--red) 100%)}
.contact .section-title{top:21px}
.field{height:27px;border:1.2px solid var(--white);display:flex;align-items:center;padding-left:7px;
  font-family:'Montserrat',sans-serif;font-weight:600;font-size:7.4px;letter-spacing:1.6px}
.send{left:306px;top:135px;width:72px;height:19px;border-radius:12px;background:#111;display:flex;align-items:center;justify-content:center;
  font-family:'Montserrat',sans-serif;font-weight:700;font-size:7px;letter-spacing:1px}

/* footer */
.footer{position:absolute;left:0;top:1063px;width:685px;height:137px;background:var(--footer);font-family:'Roboto',sans-serif}
.f-head{top:22px;font-weight:700;font-size:7.3px}
.f-text{top:39px;font-size:6px;line-height:8.1px;color:#e5e5e5;width:112px}
.f-links{top:40px;font-size:6px;line-height:11.2px;color:#e5e5e5}
.social{top:36px;display:flex;gap:2.5px}
.social span{width:15px;height:15px;border-radius:50%;background:#3a3a3e}
.social span:first-child{background:var(--red)}
.f-rule{left:0;top:107px;width:685px;height:1px;background:#2e2e31}
.f-bottom{top:118px;font-size:6px;color:#e5e5e5}
</style>
</head>
<body>

<header class="hero">
  <div class="hero-photo" role="img" aria-label="Photo of a uniformed security officer in cap and sunglasses speaking into a handheld radio"></div>
  <svg class="abs" style="left:47px;top:0" width="52" height="24" viewBox="0 0 52 24"><polygon points="0,0 52,0 26,24" fill="#e41d2d"/></svg>
  <svg class="abs" style="left:502px;top:274px" width="154" height="78" viewBox="0 0 154 78"><polygon points="78,0 154,78 0,78" fill="#e41d2d"/></svg>

  <div class="abs brand"><span class="brand-dot"></span>VARNO</div>
  <nav class="abs nav">
    <span class="active">HOME</span><span>ABOUT US</span><span>GUYANA SECURITY OVERVIEW</span><span>SERVICES</span><span>CONTACT US</span>
  </nav>
  <div class="abs phone">+1(555) 010-47-31</div>
  <div class="abs btn btn-call">CALL US TODAY</div>

  <div class="abs eyebrow">YOUR LIFE IS SAFE WITH</div>
  <h1 class="abs hero-title">VARNO</h1>
  <p class="abs hero-copy">VARNO is a fully licensed Guyanese security company offering a wide range of security services to the public and private sector and is a unique collaboration of highly trained Guyanese operatives...</p>
  <div class="abs btn btn-more">FIND OUT MORE</div>

  <div class="abs slides"><span>01</span><span class="bar"></span><span class="n">02</span><span class="n">03</span><span>04</span></div>
</header>

<div class="abs badge" style="left:323px;top:331px"><i></i></div>

<section class="services" role="img" aria-label="Background photo of suited bodyguards beside a dark vehicle">
  <h2 class="abs section-title">OUR SERVICES</h2>
  <p class="abs lead">VARNO offers the following services to protect you, your<br>colleagues, family, business or assets:</p>

  <svg class="abs arrow" style="left:88px" width="12" height="16" viewBox="0 0 12 16"><polyline points="9,1 2,8 9,15" fill="none" stroke="#fff" stroke-width="2"/></svg>
  <svg class="abs arrow" style="left:587px" width="12" height="16" viewBox="0 0 12 16"><polyline points="3,1 10,8 3,15" fill="none" stroke="#fff" stroke-width="2"/></svg>

  <div class="abs svc" style="left:114px">
    <div class="ring"><svg width="24" height="26" viewBox="0 0 24 26"><path d="M12 1 L22 5 V12 C22 19 17 23 12 25 C7 23 2 19 2 12 V5 Z" fill="none" stroke="#fff" stroke-width="1.3"/></svg></div>
    <p>UNARMED AND ARMED<br>CLOSE PROTECTION</p>
  </div>
  <div class="abs svc" style="left:236px">
    <div class="ring on"><svg width="24" height="26" viewBox="0 0 24 26"><path d="M12 1 L22 5 V12 C22 19 17 23 12 25 C7 23 2 19 2 12 V5 Z" fill="none" stroke="#fff" stroke-width="1.4"/><polyline points="7,13 11,17 17,9" fill="none" stroke="#fff" stroke-width="1.4"/></svg></div>
    <p>STATIC &amp; MOBILE SECURITY<br>(ARMED AND UNARMED)</p>
  </div>
  <div class="abs svc" style="left:352px">
    <div class="ring"><svg width="26" height="16" viewBox="0 0 26 16"><path d="M1 8 C6 1 20 1 25 8 C20 15 6 15 1 8 Z" fill="none" stroke="#fff" stroke-width="1.3"/><circle cx="13" cy="8" r="3.5" fill="none" stroke="#fff" stroke-width="1.3"/></svg></div>
    <p>ADVANCED COVERT<br>SURVEILLANCE</p>
  </div>
  <div class="abs svc" style="left:461px">
    <div class="ring"><svg width="26" height="26" viewBox="0 0 26 26"><circle cx="13" cy="13" r="10" fill="none" stroke="#fff" stroke-width="1.3"/><circle cx="13" cy="13" r="3.5" fill="none" stroke="#fff" stroke-width="1.3"/><path d="M13 0V8M13 18V26M0 13H8M18 13H26" stroke="#fff" stroke-width="1.3"/></svg></div>
    <p>PERSONNEL AND<br>ASSET TRACKING</p>
  </div>
</section>

<div class="abs badge" style="left:323px;top:612px"><i></i></div>

<section class="about">
  <div class="abs about-photo" role="img" aria-label="Photo of a security officer in cap, sunglasses and jacket with arms crossed"></div>
  <h2 class="abs about-title">ABOUT <em>VARNO</em></h2>
  <div class="abs about-rule"></div>
  <div class="abs col" style="left:99px">
    <p>VARNO is a fully licensed Guyanese security company offering a wide range of security services to the public and private sector and is a unique collaboration of highly trained Guyanese operatives and elite British military security experts.</p>
    <p>Our combination of local knowledge, contacts and resources teamed with years of active service in some of the most hostile regions in the world and high threat environments creates a highly capable, responsive and professional security service.</p>
    <p>We have years of experience of delivering effective security solutions to high net worth individuals and their families, multi-national corporations, royalty, politicians and valuable state owned and private assets.</p>
  </div>
  <div class="abs col" style="left:282px;width:152px">
    <p>We have developed the most advanced training offered to security personnel in Guyana, utilizing elite British operators and security doctrine and protocols developed over decades combined with a deep cultural understanding of the region.</p>
    <p>Our security operations are supported by the latest advanced technology and equipment and a wide-reaching intelligence network. &nbsp;Information, Technology, Training and Experience are the cornerstones of our operations.</p>
  </div>
</section>

<section class="contact" role="img" aria-label="Red-tinted background photo of a suited bodyguard beside a car">
  <h2 class="abs section-title">CONTACT US</h2>
  <div class="abs field" style="left:101px;top:57px;width:235px">NAME</div>
  <div class="abs field" style="left:349px;top:57px;width:234px">EMAIL</div>
  <div class="abs field" style="left:101px;top:94px;width:235px">PHONE NUMBER</div>
  <div class="abs field" style="left:349px;top:94px;width:234px">YOUR MESSAGE</div>
  <div class="abs send">SEND</div>
</section>

<footer class="footer">
  <div class="abs f-head" style="left:99px">About Us</div>
  <p class="abs f-text" style="left:99px">Lorem ipsum dolor sit amet, conse ctetur adipiscing elit, sed do eiusmod tempor incididunt ut labore et dolore magna aliqua.</p>

  <div class="abs f-head" style="left:228px">Our Address</div>
  <p class="abs f-text" style="left:228px;width:96px">Contact ops@varno.group for further information or to arrange a security consultation.</p>

  <div class="abs f-head" style="left:337px">Quick Links</div>
  <div class="abs f-links" style="left:337px">About us<br>Our services<br>Contact us<br>Meet team</div>
  <div class="abs f-links" style="left:397px">Privacy Policy<br>Testimonials<br>News<br>FAQ</div>

  <div class="abs f-head" style="left:469px">Follow Us</div>
  <div class="abs social" style="left:469px"><span></span><span></span><span></span></div>

  <div class="abs f-rule"></div>
  <div class="abs f-bottom" style="left:99px">Copyright © 2020 VARNO . All Rights Reserved</div>
  <div class="abs f-bottom" style="left:502px">Terms of Use &nbsp;| &nbsp;Privacy Policy</div>
</footer>

</body>
</html>
```